10-year customer thank you card

We want a greeting card that our sales reps can send to companies/customers who have been with our company for 10 or more years. We're a software company, our corporate color is blue but we also like green, orange, and purple. We'd like something rather minimal/simplistic for this card, perhaps building off our tree logo. We're really open to ideas for this one. You must use the template files that are uploaded. Copy included in 10 year thank you card file; the copy may change based on how it looks when laid out
Updates

I updated our brief. We'd prefer a sans serif font. I also uploaded a blank infographic image that includes more of our approved colors.

Industry/Entity Type

Software

Font styles to use
Sans Serif

```html
<!DOCTYPE html>
<html lang="en">
<head>
<meta charset="utf-8">
<title>Ten Years – Thank You Card</title>
<link rel="stylesheet" href="https://fonts.googleapis.com/css2?family=EB+Garamond:wght@400;500&family=Michroma&display=swap">
<style>
  :root {
    --paper: #ffffff;
    --ink: #1a1a1a;
    --brand-blue: #1a7fd0;
    --glow-light: #7ff3ff;
    --glow-mid: #2fd0f5;
    --glow-deep: #1b82dc;
    --years-coral: #ea7b74;
  }
  html, body {
    margin: 0;
    padding: 0;
    overflow: hidden;
    background: var(--paper);
  }
  .card {
    position: relative;
    width: 869px;
    height: 1200px;
    background: var(--paper);
    overflow: hidden;
  }
  .anniversary-mark {
    position: absolute;
    left: 0;
    top: 0;
    width: 869px;
    height: 560px;
  }
  .numeral {
    filter: drop-shadow(2px 3px 3px rgba(0, 0, 0, 0.35));
  }
  .years-word {
    font-family: "Michroma", sans-serif;
    font-size: 44px;
    letter-spacing: 6px;
    fill: var(--years-coral);
  }
  .inner-name {
    font-family: "EB Garamond", serif;
    font-size: 34px;
    fill: var(--brand-blue);
  }
  .signoff {
    position: absolute;
    left: 0;
    width: 869px;
    top: 888px;
    text-align: center;
    font-family: "EB Garamond", serif;
    color: var(--ink);
  }
  .company {
    display: inline-flex;
    align-items: center;
    gap: 10px;
    font-size: 38px;
    line-height: 1;
    margin: 0;
  }
  .company-dot {
    width: 26px;
    height: 26px;
    border-radius: 50%;
    background: var(--brand-blue);
  }
  .company-name {
    color: var(--ink);
  }
  .website {
    margin: 18px 0 0;
    font-size: 27px;
    letter-spacing: 1.5px;
  }
</style>
</head>
<body>
<main class="card">
  <svg class="anniversary-mark" viewBox="0 0 869 560" aria-label="10 years, set upside down">
    <defs>
      <linearGradient id="glossRing" x1="0" y1="0" x2="0.3" y2="1">
        <stop offset="0" stop-color="var(--glow-deep)"/>
        <stop offset="0.22" stop-color="var(--glow-light)"/>
        <stop offset="0.38" stop-color="#eaffff"/>
        <stop offset="0.55" stop-color="var(--glow-mid)"/>
        <stop offset="0.75" stop-color="var(--glow-deep)"/>
        <stop offset="0.9" stop-color="var(--glow-light)"/>
        <stop offset="1" stop-color="var(--glow-deep)"/>
      </linearGradient>
      <linearGradient id="glossBar" x1="0" y1="0" x2="0.4" y2="1">
        <stop offset="0" stop-color="var(--glow-deep)"/>
        <stop offset="0.3" stop-color="var(--glow-light)"/>
        <stop offset="0.5" stop-color="var(--glow-mid)"/>
        <stop offset="0.65" stop-color="#eaffff"/>
        <stop offset="0.85" stop-color="var(--glow-deep)"/>
        <stop offset="1" stop-color="var(--glow-mid)"/>
      </linearGradient>
      <clipPath id="topCut">
        <rect x="0" y="143" width="869" height="420"/>
      </clipPath>
    </defs>

    <g class="numeral" clip-path="url(#topCut)">
      <path class="numeral-zero" fill="url(#glossRing)" fill-rule="evenodd"
            d="M48 240 a281 290 0 1 0 562 0 a281 290 0 1 0 -562 0 Z
               M136 240 a193 227 0 1 0 386 0 a193 227 0 1 0 -386 0 Z"/>
      <path class="numeral-one" fill="url(#glossBar)"
            d="M637 143 H727 V438 L802 398 H813 V450 L730 503 V523 H637 Z"/>
    </g>

    <text class="inner-name" transform="rotate(180 329 262)" x="329" y="274" text-anchor="middle">Harborline</text>

    <text class="years-word" transform="rotate(180 320 98)" x="320" y="120" text-anchor="middle">YEARS</text>
  </svg>

  <footer class="signoff">
    <p class="company"><span class="company-dot"></span><span class="company-name">Harborline Software</span></p>
    <p class="website">www.harborline.com</p>
  </footer>
</main>
</body>
</html>
```